Geschäftspapiere für Angelverein
Zielgruppe
Angelverein, Naturschutz, Fischhege
Aufgabenstellung
Sehr modern, die beiden Farben aus dem Logo sollten wieder verwendet werden, sowie die Well-Form sollte aufgegriffen werden.

```html
<!DOCTYPE html>
<html lang="de">
<head>
<meta charset="utf-8">
<title>Angelgilde Moorbach – Geschäftspapiere</title>
<link rel="stylesheet" href="https://fonts.googleapis.com/css2?family=Roboto:wght@500&family=Arimo:wght@400&family=Carlito:wght@400&display=swap">
<style>
  :root {
    --blue: #11468a;
    --green: #86993b;
    --ink: #2b2b2b;
    --paper: #ffffff;
    --backdrop: #ececec;
    --rule: #cfcfcf;
    --sig-fill: #dcdcdf;
  }
  * { margin: 0; padding: 0; box-sizing: border-box; }
  html, body { width: 1200px; height: 815px; overflow: hidden; }
  body { background: var(--backdrop); position: relative; }

  .sheet {
    position: absolute; top: 61px; width: 490px; height: 693px;
    background: var(--paper); overflow: hidden;
  }
  .sheet--letter { left: 80px; }
  .sheet--blank { left: 636px; }

  .top-bar { position: absolute; top: 0; left: 0; right: 0; height: 4px; background: var(--blue); }

  .brand {
    position: absolute; top: 66px; left: 240px; width: 290px; text-align: center;
    font-family: "Roboto", sans-serif; font-weight: 500; font-size: 15px; color: var(--blue);
    letter-spacing: 0.1px;
  }

  .fold-mark { position: absolute; left: 0; width: 14px; height: 1px; background: var(--rule); }

  .sender-line {
    position: absolute; top: 122px; left: 59px;
    font-family: "Carlito", sans-serif; font-size: 4.8px; color: var(--ink);
    border-bottom: 0.5px solid var(--ink); padding-bottom: 0.5px;
  }

  .contact {
    position: absolute; top: 124px; left: 348px; padding-left: 8px;
    border-left: 0.8px solid var(--ink);
    font-family: "Carlito", sans-serif; font-size: 6.4px; line-height: 9.3px; color: var(--ink);
  }
  .contact p + p { margin-top: 2px; }
  .contact .icon { display: inline-block; width: 6px; height: 6px; vertical-align: -1px; margin-right: 2px; }

  .letter-body {
    position: absolute; top: 239px; left: 59px; width: 378px;
    font-family: "Arimo", sans-serif; font-size: 7.9px; line-height: 9.2px; color: var(--ink);
    text-align: justify;
  }
  .letter-body .salutation { margin-bottom: 9px; text-align: left; }
  .letter-body p + p { margin-top: 9px; }

  .signature { position: absolute; top: 425px; left: 59px; width: 94px; height: 22px; background: var(--sig-fill); }
  .signer-role { position: absolute; top: 452px; left: 59px; font-family: "Arimo", sans-serif; font-size: 7.9px; color: var(--ink); }

  .legal {
    position: absolute; top: 619px; left: 59px; display: flex;
    font-family: "Carlito", sans-serif; font-size: 6.3px; line-height: 8.8px; color: var(--ink);
  }
  .legal__col { padding-right: 12px; }
  .legal__col + .legal__col { border-left: 0.8px solid var(--ink); padding-left: 12px; }

  .wave { position: absolute; left: 0; bottom: 0; width: 490px; height: 47px; display: block; }
  .web {
    position: absolute; bottom: 11px; left: 59px;
    font-family: "Carlito", sans-serif; font-size: 7.6px; letter-spacing: 0.6px; color: #fff;
  }
</style>
</head>
<body>

<article class="sheet sheet--letter">
  <div class="top-bar"></div>
  <div class="brand">Angelgilde Moorbach</div>

  <span class="fold-mark" style="top:246px"></span>
  <span class="fold-mark" style="top:346px"></span>
  <span class="fold-mark" style="top:490px"></span>

  <div class="sender-line">Angelgilde Moorbach | Schilfweg 14 | 20417 Lindental</div>

  <address class="contact" style="font-style:normal">
    <p>Jonas Kettler<br>Schatzmeister</p>
    <p>Schilfweg 14<br>20417 Lindental</p>
    <p>
      <svg class="icon" viewBox="0 0 6 6"><rect x="1.5" y="0.3" width="3" height="5.4" rx="0.5" fill="none" stroke="var(--blue)" stroke-width="0.7"/></svg>+49 (0) 5800 4120 - 210<br>
      <svg class="icon" viewBox="0 0 6 6"><rect x="0.3" y="1.2" width="5.4" height="3.8" fill="var(--blue)"/><path d="M0.4 1.4 L3 3.3 L5.6 1.4" fill="none" stroke="#fff" stroke-width="0.5"/></svg>info@angelgilde-moorbach.de
    </p>
  </address>

  <section class="letter-body">
    <p class="salutation">Herr Wendlin</p>
    <p>Lorem ipsum dolor sit amet, consectetur adipiscing elit. Proin tincidunt, lectus id malesuada cursus, lorem augue egestas magna, ut mattis orci ante ut arcu. Sed mauris tellus, fermentum quis ligula nec, posuere pulvinar eros. Nam at mi quis velit pellentesque finibus. Donec lacus velit, faucibus mollis dolor nec, finibus pellentesque orci. Duis sed dictum elit, ut posuere arcu. Phasellus ac dolor et ante consequat rutrum nec nec tortor. Donec consequat, nibh sit amet pulvinar faucibus, turpis magna venenatis diam, vel pretium eros erat vestibulum nulla.</p>
    <p>Sed pretium ac enim eu viverra. Aliquam ac est eget magna convallis convallis. Aenean augue purus, finibus eget turpis quis, finibus dignissim nibh. Phasellus viverra lobortis dignissim. Duis varius turpis in sapien accumsan facilisis. Sed vehicula gravida diam a interdum. Nullam convallis ligula id erat egestas consequat. Integer consectetur ex vel aliquet iaculis. Vestibulum molestie sodales mauris, at tincidunt risus pellentesqu.</p>
    <p>Mauris facilisis, lectus at accumsan tincidunt, dui magna imperdiet sem, quis tempor est lectus eu ipsum. Praesent in fermentum nisl. Maecenas at lorem at odio interdum iaculis. Pellentesque cursus nulla nunc, ut suscipit nulla maximus et. Donec maximus rhoncus metus, vel laoreet nisi pretium sit amet. Donec posuere enim lectus, vitae aliquam augue tincidunt dignissim. Morbi vitae congue velit, quis elementum.</p>
  </section>

  <div class="signature" role="img" aria-label="Handschriftliche Unterschrift des Schatzmeisters"></div>
  <div class="signer-role">Schatzmeister</div>

  <footer class="legal">
    <div class="legal__col">Angelgilde Moorbach<br>Sitz: 20417 Lindental<br>Adresse: Uferstr. 7, 20419 Lindental-Au</div>
    <div class="legal__col">Vertretungsberechtigter Vorstand:<br>Tobias Rennwald (1. Vorsitzender)<br>Luca Ferrandi Holt (2. Vorsitzender)</div>
    <div class="legal__col">Vereinsregister<br>Registergericht: Amtsgericht Lindental<br>Registernummer: VR 40931</div>
  </footer>

  <svg class="wave" viewBox="0 0 949 90" preserveAspectRatio="none" aria-hidden="true">
    <path d="M230 15 C450 28 620 70 780 70 C860 70 915 55 949 0 L949 38 C880 62 810 68 740 66 C560 58 420 26 230 15Z" fill="var(--green)"/>
    <path d="M0 28 C250 2 500 40 700 66 C820 80 900 62 949 48 L949 90 L0 90Z" fill="var(--blue)"/>
  </svg>
  <div class="web">www.angelgilde-moorbach.de</div>
</article>

<article class="sheet sheet--blank">
  <div class="top-bar"></div>
  <div class="brand">Angelgilde Moorbach</div>

  <span class="fold-mark" style="top:246px"></span>
  <span class="fold-mark" style="top:346px"></span>
  <span class="fold-mark" style="top:490px"></span>

  <svg class="wave" viewBox="0 0 949 90" preserveAspectRatio="none" aria-hidden="true">
    <path d="M230 15 C450 28 620 70 780 70 C860 70 915 55 949 0 L949 38 C880 62 810 68 740 66 C560 58 420 26 230 15Z" fill="var(--green)"/>
    <path d="M0 28 C250 2 500 40 700 66 C820 80 900 62 949 48 L949 90 L0 90Z" fill="var(--blue)"/>
  </svg>
  <div class="web">www.angelgilde-moorbach.de</div>
</article>

</body>
</html>
```